Brookvane Estates LLC stationary for a real estate property management company.

Create stationary (letterhead, envelopes, business cards) using Brookvane Estates LLC logo as primary creative element. Stationary design needs to be horizontal, leaving as much space as possible for correspondence copy. See attached Creative Brief and past stationary files for details.

Target Market(s)

Prospective apartment residents and current residents, vendors, and government agencies.

Industry/Entity Type

Property Management

Contact Information for Business Card

Business card employee title: Property Manager. Should include address, phone, fax, email, website, slogan, and Brookvane Estates logo.

Font styles to use
Sans Serif

Colors
0592cd
000000

Requirements
Must have
• Tone should be conservative, institutional, business (i.e. banking, finance, real estate). Must include: address, phone, fax, website, and slogan (see attached Creative Brief). Should be a horizontal design, leaving as much room as possible for letter correspondence copy.
Nice to have
• Please use an Arial or Helvetica style font.
Should not have
• Letterhead layout should leave as much room as possible for copy.

```html
<!DOCTYPE html>
<html lang="en">
<head>
<meta charset="utf-8">
<title>Brookvane Estates LLC — Envelope</title>
<link rel="stylesheet" href="https://fonts.googleapis.com/css2?family=Lexend:wght@400;600&display=swap">
<style>
  :root {
    --brand-blue: #1d58a0;
    --ink: #111111;
    --paper: #ffffff;
    --rule: #d9d9d9;
    --frame: #333333;
  }
  * { margin: 0; padding: 0; box-sizing: border-box; }
  html, body {
    width: 1200px;
    height: 528px;
    overflow: hidden;
    background: var(--paper);
  }
  .envelope {
    position: relative;
    width: 1200px;
    height: 528px;
    background: var(--paper);
    border: 1px solid var(--frame);
    font-family: "Lexend", Arial, sans-serif;
  }
  .return-address {
    position: absolute;
    left: 64px;
    top: 80px;
    display: flex;
    align-items: flex-start;
    gap: 56px;
  }
  .brand-square {
    width: 96px;
    height: 96px;
    margin-top: 2px;
    background: var(--brand-blue);
  }
  .brand-block {
    width: 286px;
  }
  .brand-name {
    color: var(--brand-blue);
    font-weight: 600;
    font-size: 30px;
    line-height: 1.08;
    letter-spacing: 0.2px;
    padding-top: 2px;
  }
  .brand-rule {
    margin-top: 14px;
    height: 1px;
    background: var(--rule);
  }
  .mailing-address {
    margin-top: 15px;
    color: var(--brand-blue);
    font-weight: 400;
    font-size: 13.6px;
    letter-spacing: 0.1px;
    white-space: nowrap;
  }
</style>
</head>
<body>
  <main class="envelope">
    <section class="return-address">
      <div class="brand-square" aria-hidden="true"></div>
      <div class="brand-block">
        <h1 class="brand-name">Brookvane<br>Estates LLC</h1>
        <div class="brand-rule"></div>
        <p class="mailing-address">2780 Harbor Crest Dr. #310, San Diego, CA 92110</p>
      </div>
    </section>
  </main>
</body>
</html>
```